Art Wall - Illustrates "Be Colorful"

I have a seasonal color business called Porch Step Blooms. We plant containers and add colorful annuals to garden beds. I need a 6' tall by 18' long banner that will be hung on a wall or possibly used on the side of my enclosed trailer. The banner will be used as backdrop for ladies taking pictures together and as a backdrop for colorful container gardens to be photographed for our website. It should have the words "Be Colorful" on it. I would like for it to look like a fun art wall that you would take a picture in front of in a downtown area. The art should work well with our logo. We love flowers but other ideas are welcome. Feel free to look at our instagram @porchstepbloomsokc to see examples of our work. I have uploaded our logo and a colorful flower picture we liked (great colors) but didn't quite work with our logo and a fun colorful wall at a restaurant that we really like.

Target Market(s)

women ages 30-45, wealthy, like to feel like they are trendy

Industry/Entity Type

Landscape Gardening

Font styles to use
Serif

Requirements
Must have
• The words "Be Colorful" on it and some space that would good for people to stand or objects to be placed to be photographed.
Nice to have
• We really like the colors in the "sun's out now" t-shirt picture I have attached. Also like the watercolor, alcohol ink, or hand-painted look.
Should not have
• Please do not include our logo on the banner. It will be added as a watermark to our photos.

Please do not literally use the logo flower in the design. Feel free to use pieces or inspiration from the logo but the wall should look more like art and less like a cartoon.

```html
<!DOCTYPE html>
<html lang="en">
<head>
<meta charset="utf-8">
<title>Be Colorful – Art Wall Banner</title>
<link rel="stylesheet" href="https://fonts.googleapis.com/css2?family=Playfair+Display:ital,wght@1,700&display=swap">
<style>
  :root {
    --canvas-w: 1200px;
    --canvas-h: 399px;
    --paper: #ffffff;
    --tone-violet: #b9a6d8;
    --tone-teal: #8fd3cf;
    --tone-rose: #d9577a;
    --tone-blue: #4f93b3;
    --tone-sun: #f4d46a;
    --tone-peach: #f5a96a;
    --ink-marigold: #d9a055;
    --ink-olive: #6b6650;
    --ink-linen: #e2cbb5;
    --ink-coral: #dd6a4a;
    --ink-taupe: #b8ada0;
    --ink-moss: #5d5b48;
    --ink-slate: #7a7c78;
  }
  * { margin: 0; padding: 0; box-sizing: border-box; }
  html, body {
    width: var(--canvas-w);
    height: var(--canvas-h);
    overflow: hidden;
    background: var(--paper);
  }
  .banner {
    position: relative;
    width: var(--canvas-w);
    height: var(--canvas-h);
    overflow: hidden;
  }
  .watercolor-field {
    position: absolute;
    inset: 0;
    background:
      radial-gradient(ellipse 46% 70% at 50% 50%, rgba(255,255,255,0.95) 0%, rgba(255,255,255,0.7) 45%, rgba(255,255,255,0) 100%),
      linear-gradient(180deg,
        var(--tone-violet) 0%, var(--tone-peach) 14%, var(--tone-rose) 24%,
        var(--tone-teal) 36%, var(--tone-sun) 48%, var(--tone-blue) 58%,
        var(--tone-violet) 70%, var(--tone-teal) 80%, var(--tone-rose) 92%, var(--tone-sun) 100%);
    opacity: 0.85;
  }
  .headline {
    position: absolute;
    left: 0;
    right: 0;
    top: 92px;
    text-align: center;
    font-family: "Playfair Display", Georgia, serif;
    font-style: italic;
    font-weight: 700;
    font-size: 104px;
    line-height: 1;
    letter-spacing: -1px;
    text-shadow: 0 0 2px var(--paper), 0 0 3px var(--paper);
  }
  .headline .word + .word { margin-left: 0.28em; }
  .c-marigold { color: var(--ink-marigold); }
  .c-olive { color: var(--ink-olive); }
  .c-linen { color: var(--ink-linen); }
  .c-coral { color: var(--ink-coral); }
  .c-taupe { color: var(--ink-taupe); }
  .c-moss { color: var(--ink-moss); }
  .c-slate { color: var(--ink-slate); }
</style>
</head>
<body>
  <main class="banner">
    <div class="watercolor-field" role="img" aria-label="Watercolor pattern of repeating triangles in violet, teal, rose, blue, yellow and peach, fading to white in the centre"></div>
    <h1 class="headline">
      <span class="word c-marigold">Be</span><span class="word"><span class="c-olive">C</span><span class="c-linen">o</span><span class="c-coral">l</span><span class="c-taupe">o</span><span class="c-moss">r</span><span class="c-slate">ful</span></span>
    </h1>
  </main>
</body>
</html>
```